Website: Brightkeel Business Consultants, Harbourline Trade District

Our client is a business consultancy firm and will be the first to set up in the Qianhai Shenzhen-Hong Kong Modern Service Industry Cooperation Zone, China So we need a corporate website concept that engages service, finance and technology sector companies. The company can provide all the necessary services needed to set up shop in Qianhai. They are looking for a modern, international, reliable and strong image.

Here are some websites for reference prupose:

http://www.vornamesh.com/ (we like the dynamic banner and clear, clean layout of this website)

http://www.plendaradvisory.com/ (we like the background city image, use of light font, hover over menu functions and color scheme - purple and grey)

http://www.quolb.com/ (we like the simplicity of this website, clear lines and we like the dynamic banner)
Updates

Hello, We are currently undecided between three logo designs.  All three have been uploaded to the design brief so that you can use them as reference for the website design. Thx

Also please take note of the addition menu selection 'About Qianhai'. Thx

Hello all Designers, First of all we want thank you for participating in our website competition, the calibre of design was high and we appreciated the expedience. Our company is Lumenpath Web Design and Internet Marketing based in Shenzhen, China. We anticipate rapid growth in the Chinese domestic market as the country shifts in to a service sector economy. We hope to continue building reliable working relationships with you based on idea sharing and constructive feedback. Once again, Thankyou, LP Team

Target Market(s)

International finance and technology companies looking to set up in Qianhai Special Economic Zone, China

Industry/Entity Type

Finance

Requirements
Must have
• Initial design for home page and in later selection stages a secondary page will be required.

The design should be for PSD concepts only no code!

Menu bar, Photo banner -
A. Photo banner and text overlay,
B.Photo Banner and text description to left or right.

Social Connect icons, Site search bar (top right), Logo space (top left).

Menu bar at top with Home, About Us, About Qianhai, Services, Portfolio, Partners, Our Team Contact Us.

Standard 3-4 box layout - Banner at top and 2-3 boxes under banner.

Colour scheme- A. Purple and Blue, must have light background/body
B. Shades of white, black and grey.

Simple, clear, clean, sharp.

```html
<!DOCTYPE html>
<html lang="en">
<head>
<meta charset="utf-8">
<title>Brightkeel Business Consultants</title>
<link rel="stylesheet" href="https://fonts.googleapis.com/css2?family=Roboto:wght@300;400;500;700&display=swap">
<style>
  :root {
    --page-edge: #c9c9cb;
    --page-centre: #ffffff;
    --ink: #2b2b2e;
    --muted: #6d6d72;
    --blue-band: #2c6ab8;
    --purple: #6a3597;
    --purple-band: #6e3698;
    --blue-link: #2a66bd;
    --purple-link: #6b3a9e;
    --accent: #8a3fc4;
    --white: #ffffff;
    --line: #cfcfd4;
  }
  * { box-sizing: border-box; margin: 0; padding: 0; }
  html, body { width: 1200px; height: 960px; overflow: hidden; }
  body {
    position: relative;
    font-family: "Roboto", Arial, sans-serif;
    color: var(--ink);
    background: radial-gradient(ellipse 62% 60% at 50% 48%, var(--page-centre) 55%, var(--page-edge) 100%);
  }
  .utility-bar { position: absolute; top: 19px; left: 607px; display: flex; align-items: center; }
  .language-select { font-size: 12px; color: var(--muted); display: flex; align-items: center; gap: 18px; width: 134px; }
  .language-select svg { width: 9px; height: 7px; }
  .site-search {
    width: 200px; height: 33px; border: 1px solid var(--line); background: var(--white);
    display: flex; align-items: center; justify-content: space-between; padding: 0 10px 0 12px;
    font-size: 12px; color: #8a8a90;
  }
  .hero {
    position: absolute; left: 159px; top: 86px; width: 882px; height: 523px;
    background:
      radial-gradient(ellipse 45% 55% at 58% 68%, #d6e9fb 0%, rgba(214,233,251,0) 70%),
      linear-gradient(100deg, #0c1f4f 0%, #1f4f9b 22%, #4d90dc 42%, #7fbcef 58%, #5aa6ee 78%, #2a7df4 100%);
  }
  .site-header { position: absolute; left: 234px; top: 86px; width: 732px; height: 66px; background: var(--white); }
  .brand { position: absolute; left: 31px; top: -26px; display: flex; align-items: center; gap: 14px; }
  .brand-mark { width: 62px; height: 62px; background: var(--purple); }
  .brand-name { font-size: 25px; font-weight: 500; color: var(--ink); letter-spacing: -0.3px; }
  .main-nav { position: absolute; left: 320px; top: 12px; display: flex; }
  .main-nav a { font-size: 17px; font-weight: 500; color: var(--ink); text-decoration: none; }
  .main-nav a:nth-child(1) { width: 94px; }
  .main-nav a:nth-child(2) { width: 103px; }
  .main-nav a:nth-child(3) { width: 103px; }
  .hero-title {
    position: absolute; left: 634px; top: 230px; white-space: nowrap;
    font-size: 37px; font-weight: 300; line-height: 43px; color: var(--white); letter-spacing: -1px;
  }
  .hero-title a { color: var(--accent); text-decoration: underline; text-decoration-thickness: 1px; text-underline-offset: 5px; }
  .hero-title .arrow { color: var(--accent); }
  .feature-box { position: absolute; top: 433px; width: 357px; height: 232px; color: var(--white); }
  .feature-about { left: 234px; background: rgba(38,104,190,0.92); }
  .feature-services { left: 609px; background: var(--purple); }
  .feature-box h2 { position: absolute; left: 36px; top: 27px; font-size: 31px; font-weight: 300; }
  .feature-services h2 { left: 37px; top: 24px; }
  .feature-box p { position: absolute; left: 33px; top: 82px; width: 310px; font-size: 15px; line-height: 22.5px; font-weight: 300; letter-spacing: -0.2px; }
  .feature-services p { left: 37px; top: 80px; width: 315px; }
  .feature-more {
    position: absolute; left: 0; bottom: 0; width: 100%; height: 56px; padding: 15px 0 0 32px;
    font-size: 15px; font-weight: 700; letter-spacing: -0.2px; color: var(--white);
  }
  .feature-about .feature-more { background: var(--blue-band); }
  .feature-services .feature-more { background: var(--purple-band); padding-left: 37px; }
  .sitemap { position: absolute; top: 697px; left: 0; width: 100%; }
  .sitemap-column { position: absolute; top: 0; }
  .sitemap-column h3 { font-size: 17px; font-weight: 500; margin-bottom: 12px; }
  .sitemap-column li { list-style: none; font-size: 13.5px; line-height: 22.5px; }
  .tone-blue h3, .tone-blue li { color: var(--blue-link); }
  .tone-purple h3, .tone-purple li { color: var(--purple-link); }
  .copyright { position: absolute; top: 902px; left: 0; width: 100%; text-align: center; font-size: 11px; color: #7a7a80; }
</style>
</head>
<body>
  <div class="utility-bar">
    <div class="language-select">Choose language
      <svg viewBox="0 0 9 7"><path d="M0 0h9L4.5 7z" fill="#2a5fc4"/></svg>
    </div>
    <div class="site-search">Search the site
      <svg width="20" height="18" viewBox="0 0 20 18"><circle cx="7" cy="7" r="5" fill="none" stroke="#8a3fc4" stroke-width="2"/><path d="M11 10l7 6" stroke="#8a3fc4" stroke-width="3" stroke-linecap="round"/></svg>
    </div>
  </div>

  <div class="hero" role="img" aria-label="Photo of a glass skyscraper rising into a bright blue sky"></div>

  <header class="site-header">
    <div class="brand">
      <span class="brand-mark"></span>
      <span class="brand-name">Brightkeel</span>
    </div>
    <nav class="main-nav">
      <a href="#">Services</a>
      <a href="#">Industries</a>
      <a href="#">Company</a>
      <a href="#">News</a>
    </nav>
  </header>

  <h1 class="hero-title">Lorem ipsum dolor sit<br>amet, consectetuer<br>adipiscing <a href="#">elit</a> <span class="arrow">›</span></h1>

  <section class="feature-box feature-about">
    <h2>About us</h2>
    <p>Donec nec justo eget felis facilisis fermentum. Aliquam porttitor mauris sit amet orci. Aenean dignissim pellentesque felis.</p>
    <div class="feature-more">Read more ›</div>
  </section>
  <section class="feature-box feature-services">
    <h2>What we do?</h2>
    <p>Morbi in sem quis dui placerat ornare. Pellentesque odio nisi, euismod in, pharetra a, ultricies in, diam. Sed arcu. Cras consequat.</p>
    <div class="feature-more">Read more ›</div>
  </section>

  <footer class="sitemap">
    <div class="sitemap-column tone-blue" style="left:237px">
      <h3>Services</h3>
      <ul><li>› Lorem ipsum</li><li>› Aliquam tincidunt</li><li>› Vestibulum auctor</li><li>› Nunc dignissim</li><li>› Cras ornare</li></ul>
    </div>
    <div class="sitemap-column tone-blue" style="left:415px">
      <h3>Industries</h3>
      <ul><li>› Lorem ipsum</li><li>› Aliquam tincidunt</li><li>› Vestibulum auctor</li><li>› Nunc dignissim</li><li>› Cras ornare</li></ul>
    </div>
    <div class="sitemap-column tone-purple" style="left:629px">
      <h3>Company</h3>
      <ul><li>› Lorem ipsum</li><li>› Aliquam tincidunt</li><li>› Vestibulum auctor</li><li>› Nunc dignissim</li><li>› Cras ornare</li></ul>
    </div>
    <div class="sitemap-column tone-purple" style="left:807px">
      <h3>News</h3>
      <ul><li>› Lorem ipsum</li><li>› Aliquam tincidunt</li><li>› Vestibulum auctor</li><li>› Nunc dignissim</li><li>› Cras ornare</li></ul>
    </div>
  </footer>

  <p class="copyright">Copyright © 2013 Brightkeel Business Consultants, Harbourline Trade District</p>
</body>
</html>
```